Oil and Gas Letterhead Design Tweak

Simple letterhead information and design tweak.

Please note, we don't want to change the design or logo of the letterhead only the small changes mentioned below.

We need to change the company name up top to "Northvale Petrotech Kestra"

Also, we need to include in the footer the following information. I have attached an image of roughly how we would like to have it displayed in the footer.

Footer Details:

Northvale Petrotech Kestra,
Unit No. 7283, Kestra Business Center, level No. 2, R&P 8, Dubai, United Arab Emirates
Northvale Petrotech Kestra is registered as a free zone company under the rules & regulations of Kestra

Target Market(s)

O&G Market

Industry/Entity Type

Oil And Gas

Font styles to use
Sans Serif

Colors

Designer to choose colors to be used in the design.

Requirements
Must have
• Change the company name to Northvale Petrotech Kestra
• Include the footer on the bottom of the first and continuation page
Should not have
• Should not change the design or logo of the letterhead, only the specified changes mentioned above

```html
<!DOCTYPE html>
<html lang="en">
<head>
<meta charset="utf-8">
<title>Northvale Petrotech Kestra — Letterhead</title>
<link href="https://fonts.googleapis.com/css2?family=Lato:wght@300;400;700&family=Roboto:wght@400;500;700&display=swap" rel="stylesheet">
<style>
  :root {
    --backdrop: #e9e9e9;
    --paper: #ffffff;
    --brand-blue: #1450a3;
    --brand-red: #e31e24;
    --ink-dark: #1d1d1f;
    --ink-body: #6b6b6b;
    --ink-muted: #8a8a8a;
    --ink-footer: #555555;
  }
  * { margin: 0; padding: 0; box-sizing: border-box; }
  html, body {
    width: 1200px; height: 1200px; overflow: hidden;
    background: var(--backdrop);
  }
  .letterhead {
    position: absolute; left: 192px; top: 23px;
    width: 816px; height: 1154px;
    background: var(--paper);
    overflow: hidden;
    font-family: "Lato", sans-serif;
    color: var(--ink-body);
  }
  .top-band { position: absolute; top: 0; height: 15px; }
  .top-band--blue {
    left: 0; width: 187px; background: var(--brand-blue);
    clip-path: polygon(0 0, 100% 0, calc(100% - 7px) 100%, 0 100%);
  }
  .top-band--red {
    left: 254px; right: 0; background: var(--brand-red);
    clip-path: polygon(0 0, 100% 0, 100% 100%, 6px 100%);
  }
  .company-name {
    position: absolute; left: 0; right: 0; top: 50px;
    text-align: center;
    font-family: "Roboto", sans-serif; font-weight: 700;
    font-size: 22px; letter-spacing: -0.2px;
    color: var(--ink-dark);
    text-transform: uppercase;
  }
  .letter {
    position: absolute; left: 74px; width: 668px; top: 288px;
  }
  .recipient-label { font-size: 13px; color: var(--ink-muted); }
  .recipient-name {
    margin-top: 24px; font-size: 17px; font-weight: 700; color: var(--ink-muted);
  }
  .recipient-role { margin-top: 1px; font-size: 11px; color: var(--ink-muted); }
  .recipient-contact {
    margin-top: 20px; font-size: 11px; line-height: 17px; color: var(--ink-muted);
  }
  .recipient-contact b { font-weight: 400; font-size: 13px; }
  .salutation { margin-top: 29px; font-size: 14px; color: var(--ink-muted); }
  .intro {
    margin-top: 18px; font-size: 11px; line-height: 20.5px; color: var(--ink-body);
  }
  .body-text {
    margin-top: 17px; font-size: 13.5px; line-height: 23.1px;
    font-weight: 300; color: var(--ink-body); text-align: justify;
  }
  .body-text + .body-text { margin-top: 23px; }
  .footer {
    position: absolute; left: 0; right: 0; top: 1070px;
    text-align: center; font-family: "Roboto", sans-serif;
    font-size: 12px; line-height: 18px; color: var(--ink-footer);
  }
  .footer-title { font-weight: 700; color: var(--ink-dark); text-transform: uppercase; }
  .footer-sep { margin: 0 5px; }
  .corner-mark { position: absolute; bottom: 0; height: 14px; }
  .corner-mark--blue {
    left: 592px; width: 41px; background: var(--brand-blue);
    clip-path: polygon(8px 0, 100% 0, calc(100% - 8px) 100%, 0 100%);
  }
  .corner-mark--red {
    left: 636px; width: 40px; background: var(--brand-red);
    clip-path: polygon(8px 0, calc(100% - 8px) 0, 100% 100%, 0 100%);
  }
</style>
</head>
<body>
<main class="letterhead">
  <div class="top-band top-band--blue"></div>
  <div class="top-band top-band--red"></div>

  <h1 class="company-name">Northvale Petrotech Kestra</h1>

  <section class="letter">
    <p class="recipient-label">To</p>
    <p class="recipient-name">Maren Holt</p>
    <p class="recipient-role">Director</p>
    <p class="recipient-contact">
      <b>P:</b> (02) 555 014 2087<br>
      <b>E:</b> mholt@northvale-example.com<br>
      www.northvale-example.com
    </p>
    <p class="salutation">Dear Sir</p>
    <p class="intro">Lorem ipsum dolor sit amet, consectetur adipiscing elit. Donec orci purus, luctus vitae dignissim eu, iaculis sed purus. Vivamus faucibus, ipsum nec aliquet viverra, leo mauris condimentum ligula, sit amet sagittis enim ligula quis arcu. Nam egestas tortor id nisi porttitor mattis. In tortor ante, ultricies in suscipit a, tempus non massa. Vivamus et auctor mi. Fusce vel massa null</p>
    <p class="body-text">Phasellus nec eros mauris, et scelerisque orci. Donec malesuada orci vitae nulla accumsan porta a id massa. Quisque accumsan iaculis magna sit amet fringilla. Maecenas consequat, magna eget tincidunt semper, odio nibh rutrum mi, id feugiat ante nisi eu risus. Vestibulum nunc orci, rhoncus a placerat in, ultricies in mi. Cras mattis varius eros, vel fringilla nisi suscipit eget.</p>
    <p class="body-text">Quisque scelerisque sagittis nulla at porttitor. Mauris a justo et tellus interdum tristique. Sed id augue vitae urna euismod commodo aliquet a quam. Pellentesque arcu velit, cursus et malesuada. Quisque scelerisque sagittis nulla at porttitor. Mauris a justo et tellus interdum tristique. Sed id augue vitae urna euismod commodo aliquet a quam. Pellentesque arcu velit, cursus et malesuada.&nbsp; Mauris a justo et tellus interdum tristique. Sed id augue vitae urna euismod commodo aliquet a quam. cursus et malesuada. Quisque scelerisque sagittis nulla at porttitor. Mauris a justo et tellus interdum tristique. Sed id augue vitae urna euismod commodo aliquet a quam. Pellentesque arcu velit, cursus et malesuada.&nbsp; Mauris a justo et tellus interdum tristique. Sed id augue vitae urna euismod commodo aliquet a quam.</p>
  </section>

  <footer class="footer">
    <p class="footer-title">Northvale Petrotech Kestra</p>
    <p>Unit No. 7283<span class="footer-sep">|</span> Kestra Business Center<span class="footer-sep">|</span> level No. 2, R&amp;P 8<span class="footer-sep">|</span> Dubai<span class="footer-sep">|</span> United Arab Emirates</p>
    <p>Northvale Petrotech Kestra is registered as a free zone company under the rules &amp; regulations of Kestra</p>
  </footer>

  <div class="corner-mark corner-mark--blue"></div>
  <div class="corner-mark corner-mark--red"></div>
</main>
</body>
</html>
```